" Atendemos de maneira integrada em reabilitação ,tanto odontológica como neurológica. Somos terapia ocupacional, fonoaudiologia, neuropediatria e odontologia. Trabalhamos com técnicas de ponta e muito proximidade com nossos pacientes e suas famílias. "

```html
<!DOCTYPE html>
<html lang="pt-BR">
<head>
<meta charset="UTF-8">
<title>Clarivita — Papel Timbrado</title>
<link rel="stylesheet" href="https://fonts.googleapis.com/css2?family=Montserrat:wght@400;800&display=swap">
<style>
  :root {
    --backdrop: #e9e6e1;
    --paper: #ffffff;
    --brand-navy: #1f4f8a;
    --brand-green: #8cc63f;
    --brand-blue: #2b9ed8;
    --text-grey: #6b6f75;
    --mark-grey: #ecedef;
  }
  * { margin: 0; padding: 0; box-sizing: border-box; }
  html, body { width: 1200px; height: 1200px; overflow: hidden; }
  body {
    background: var(--backdrop);
    font-family: "Montserrat", sans-serif;
    position: relative;
  }
  .letterhead {
    position: absolute;
    left: 246px;
    top: 100px;
    width: 707px;
    height: 1000px;
    background: var(--paper);
    box-shadow: 0 6px 18px rgba(0,0,0,0.18);
    overflow: hidden;
  }
  .brand {
    position: absolute;
    left: 40px;
    top: 36px;
  }
  .brand-name {
    display: flex;
    align-items: center;
    gap: 10px;
    font-weight: 800;
    font-size: 26px;
    letter-spacing: 0.5px;
    color: var(--brand-navy);
  }
  .brand-dot {
    width: 22px; height: 22px; border-radius: 50%;
    background: var(--brand-green);
  }
  .brand-tagline {
    margin-top: 3px;
    font-size: 9px;
    letter-spacing: 1px;
    text-transform: uppercase;
    color: var(--brand-navy);
  }
  .brand-watermark {
    position: absolute;
    left: 90px;
    top: 255px;
    width: 420px;
    height: 420px;
    border-radius: 50%;
    background: radial-gradient(circle, var(--mark-grey) 0%, rgba(236,237,239,0.4) 70%, rgba(236,237,239,0) 100%);
  }
  .contact {
    position: absolute;
    right: 40px;
    bottom: 40px;
    list-style: none;
    text-align: right;
    font-size: 10px;
    line-height: 16px;
    color: var(--text-grey);
  }
  .contact li { display: flex; justify-content: flex-end; align-items: center; gap: 6px; }
  .contact svg { width: 10px; height: 10px; fill: var(--brand-navy); }
  .contact .icon-circle { width: 9px; height: 9px; border-radius: 50%; background: var(--brand-navy); }
  .footer-band {
    position: absolute;
    left: 0; right: 0; bottom: 0;
    height: 10px;
  }
  .footer-band .band-green {
    position: absolute; left: 0; bottom: 0;
    width: 62%; height: 5px;
    background: var(--brand-green);
  }
  .footer-band .band-blue {
    position: absolute; right: 0; bottom: 0;
    width: 38%; height: 10px;
    background: var(--brand-blue);
  }
</style>
</head>
<body>
  <main class="letterhead">
    <header class="brand">
      <div class="brand-name"><span class="brand-dot"></span>CLARIVITA</div>
      <div class="brand-tagline">Saúde Bucal &amp; Neurológica</div>
    </header>

    <div class="brand-watermark" role="img" aria-label="Marca da clínica em grande escala, esmaecida ao fundo"></div>

    <ul class="contact">
      <li>clarivita <span class="icon-circle"></span></li>
      <li>contato@clarivita.com
        <svg viewBox="0 0 10 10"><path d="M0 2h10v6H0z M0 2l5 3.5L10 2" fill="none" stroke="#1f4f8a" stroke-width="1"/></svg>
      </li>
      <li>(00) 0000-0000
        <svg viewBox="0 0 10 10"><path d="M2 0.5l2 2-1 1.3c.7 1.4 1.8 2.5 3.2 3.2l1.3-1 2 2-1.2 1.5C4.5 9.3.7 5.5.5 1.7z"/></svg>
      </li>
      <li>rua sem nome, 00 Bairro Sem Nome
        <svg viewBox="0 0 10 10"><path d="M5 0a3.4 3.4 0 0 0-3.4 3.4C1.6 6 5 10 5 10s3.4-4 3.4-6.6A3.4 3.4 0 0 0 5 0zm0 4.8a1.4 1.4 0 1 1 0-2.8 1.4 1.4 0 0 1 0 2.8z"/></svg>
      </li>
      <li>Cidade Sem Nome</li>
    </ul>

    <div class="footer-band">
      <span class="band-green"></span>
      <span class="band-blue"></span>
    </div>
  </main>
</body>
</html>
```